Business card design needed

Business Card design required for new small plumbing business.
Would like a logo/text look that is simple and unique and does not have to be representative of a plumbing company (ie. having a cartoon plumber or toilet etc) as the companyname is self explanatory.
Would like the main colour to be green (lime green).

Industry/Entity Type

Plumber

Contact Information for Business Card

BRISCOMB PLUMBING
ABN 61 947 205 318 004

Harold Tenfield
Licensed Plumber 71635
Phone: 0477 261 408

27 Worrell Drive,
Langwarrin. 3910 Victoria

Email: briscombplumbing@mailora.net

Logo Text

Briscomb Plumbing

Logo styles of interest
Character Logo
Wordmark Logo
Lettermark Logo

```html
<!DOCTYPE html>
<html lang="en">
<head>
<meta charset="utf-8">
<title>Briscomb Plumbing – Business Card</title>
<link rel="stylesheet" href="https://fonts.googleapis.com/css2?family=Signika:wght@400;600;700&display=swap">
<style>
  :root {
    --lime: #b4cb12;
    --ink: #58595b;
    --paper: #ffffff;
  }
  * { margin: 0; padding: 0; box-sizing: border-box; }
  html, body {
    width: 1200px;
    height: 693px;
    overflow: hidden;
    background: var(--paper);
  }
  .card {
    position: relative;
    width: 1200px;
    height: 693px;
    background: var(--paper);
    font-family: "Signika", "Helvetica Neue", Arial, sans-serif;
    color: var(--ink);
  }
  .brand {
    position: absolute;
    left: 64px;
    top: 0;
    width: 372px;
    color: var(--lime);
    font-weight: 600;
  }
  .brand-word {
    position: absolute;
    left: 0;
    white-space: nowrap;
  }
  .brand-word--main {
    top: 268px;
    font-size: 64px;
    line-height: 80px;
    letter-spacing: 0.13em;
  }
  .brand-word--trade {
    top: 352px;
    font-size: 46px;
    line-height: 60px;
    letter-spacing: 0.43em;
  }

  .person {
    position: absolute;
    left: 495px;
    top: 112px;
    font-weight: 600;
    font-size: 44px;
    line-height: 66px;
    white-space: nowrap;
  }

  .contacts {
    position: absolute;
    left: 495px;
    top: 270px;
    font-weight: 400;
    font-size: 43px;
    line-height: 57px;
    white-space: nowrap;
  }
  .contact-row {
    display: grid;
    grid-template-columns: 38px auto;
  }
  .contact-label { color: var(--lime); }
  .contact-value .indent { display: block; padding-left: 6px; }

  .abn {
    position: absolute;
    left: 495px;
    top: 536px;
    font-size: 33px;
    line-height: 40px;
    white-space: nowrap;
  }
</style>
</head>
<body>
  <main class="card">
    <div class="brand" aria-label="Briscomb Plumbing">
      <span class="brand-word brand-word--main">BRISCOMB</span>
      <span class="brand-word brand-word--trade">PLUMBING</span>
    </div>

    <div class="person">
      <div class="person-name">Harold Tenfield</div>
      <div class="person-licence">Licensed Plumber 71635</div>
    </div>

    <div class="contacts">
      <div class="contact-row">
        <span class="contact-label">P</span>
        <span class="contact-value">0477 261 408</span>
      </div>
      <div class="contact-row">
        <span class="contact-label">A</span>
        <span class="contact-value">27 Worrell Drive,<span class="indent">Carrowdale, 2847 Westland</span></span>
      </div>
      <div class="contact-row">
        <span class="contact-label">E</span>
        <span class="contact-value">briscombplumbing@mailora.net</span>
      </div>
    </div>

    <div class="abn">ABN 61 947 205 318 004</div>
  </main>
</body>
</html>
```